Graphic to show easy steps to find financial clarity

Howdy-I need a graphic that describe my Coin Compass Method.The attached is a concept, but please use your own creativity to show how you would display this:- There are 5 steps the process (and then we repeat/recalculate)- And three bullets that drive home the results of the processI've also attached my logo. Please use the colors in my logo and maybe add a soft green as needed.The reader should be able to briefly scan this document and understand that this is an easy/simple process that tells them how to manage their cash.Thanks!-Ned

Target Market(s)

wealthy women, whether single or married

Requirements
Must have
• Please use the colors in my logo and a soft green if needed
Should not have
• This should be a very easy to read graphic that communicates how simple/easy this is to do.

```html
<!DOCTYPE html>
<html lang="en">
<head>
<meta charset="utf-8">
<title>Coin Compass Method</title>
<link rel="stylesheet" href="https://fonts.googleapis.com/css2?family=Source+Sans+3:wght@400;500;600;700&display=swap">
<style>
  :root {
    --navy: #123b7e;
    --navy-deep: #0d2f68;
    --slate: #5f5f60;
    --ink: #4a5163;
    --icon: #4b4f5a;
    --white: #ffffff;
    --bg-left: #cdcdcf;
    --bg-mid: #dcdcde;
    --bg-light: #f6f6f7;
    --dash: #5a5a5c;
  }
  * { box-sizing: border-box; margin: 0; padding: 0; }
  html, body { width: 1200px; height: 800px; overflow: hidden; }
  body { font-family: "Source Sans 3", "Helvetica Neue", Arial, sans-serif; }

  .canvas {
    position: relative;
    width: 1200px;
    height: 800px;
    overflow: hidden;
    background: linear-gradient(90deg, var(--bg-left) 0%, var(--bg-mid) 55%, var(--bg-light) 82%, #e4e4e6 100%);
  }

  .orbit { position: absolute; left: 0; top: 0; }

  .hub {
    position: absolute;
    left: -273px; top: 127px;
    width: 546px; height: 546px;
    border-radius: 50%;
    background: var(--navy);
  }
  .hub-title {
    position: absolute;
    left: 32px; top: 288px;
    color: var(--white);
    font-weight: 700;
    font-size: 38px;
    letter-spacing: 2px;
    line-height: 81px;
  }

  .step-num {
    position: absolute;
    width: 76px; height: 76px;
    margin: -38px 0 0 -38px;
    border-radius: 50%;
    background: var(--navy);
    color: var(--white);
    font-weight: 700;
    font-size: 28px;
    display: flex; align-items: center; justify-content: center;
    box-shadow: 0 0 0 3px rgba(255,255,255,0.15);
  }
  .repeat-pill {
    position: absolute;
    left: 57px; top: 697px;
    width: 181px; height: 64px;
    border-radius: 32px;
    background: var(--navy);
    color: var(--white);
    font-weight: 700;
    font-size: 27px;
    letter-spacing: 1px;
    display: flex; align-items: center; justify-content: center;
  }

  .ribbon { position: absolute; }
  .ribbon svg.frame { position: absolute; left: 0; top: 0; }
  .ribbon-body {
    position: absolute; inset: 0;
    display: flex; align-items: center;
  }
  .ribbon-icon { position: absolute; top: 50%; margin-top: -22px; width: 44px; height: 44px; }
  .ribbon-label {
    position: absolute; top: 50%;
    transform: translateY(-50%);
    color: var(--ink);
    font-size: 19px;
    font-weight: 500;
    line-height: 27px;
    text-align: center;
    text-transform: uppercase;
    letter-spacing: 0.3px;
  }

  .result {
    position: absolute;
    left: 835px; width: 329px;
    border-radius: 38px;
    color: var(--white);
    font-weight: 600;
    font-size: 23px;
    letter-spacing: 1.4px;
    line-height: 35px;
    text-align: center;
    text-transform: uppercase;
    display: flex; align-items: center; justify-content: center;
  }
  .result--navy { background: var(--navy); }
  .result--slate { background: var(--slate); }
  .result--lifestyle { top: 51px; height: 228px; line-height: 36px; }
  .result--spend { top: 304px; height: 191px; line-height: 32px; }
  .result--base { top: 533px; height: 192px; line-height: 31px; }
</style>
</head>
<body>
<main class="canvas">

  <svg class="orbit" width="1200" height="800" viewBox="0 0 1200 800" aria-hidden="true">
    <circle cx="0" cy="400" r="350" fill="none" stroke="var(--dash)" stroke-width="4" stroke-dasharray="14 12"/>
  </svg>

  <div class="hub"></div>
  <h1 class="hub-title">COIN<br>COMPASS<br>METHOD</h1>

  <div class="step-num" style="left:123px;top:70px">01</div>
  <div class="step-num" style="left:285px;top:203px">02</div>
  <div class="step-num" style="left:342px;top:336px">03</div>
  <div class="step-num" style="left:340px;top:467px">04</div>
  <div class="step-num" style="left:282px;top:599px">05</div>
  <div class="repeat-pill">REPEAT</div>

  <!-- Step 1 -->
  <div class="ribbon" style="left:332px;top:15px;width:482px;height:112px">
    <svg class="frame" width="482" height="112" viewBox="0 0 482 112" aria-hidden="true">
      <polygon points="40,0 442,0 482,56 442,112 40,112 0,56" fill="var(--navy)"/>
      <polygon points="56,12 426,12 448,56 426,100 56,100 34,56" fill="var(--white)"/>
    </svg>
    <svg class="ribbon-icon" style="left:108px" viewBox="0 0 44 44" aria-hidden="true" fill="none" stroke="var(--icon)" stroke-width="2.4" stroke-linejoin="round">
      <rect x="4" y="28" width="6" height="12" fill="var(--icon)"/>
      <rect x="14" y="22" width="6" height="18" fill="var(--icon)"/>
      <rect x="24" y="26" width="6" height="14" fill="var(--icon)"/>
      <rect x="34" y="16" width="6" height="24" fill="var(--icon)"/>
      <polyline points="4,22 16,12 26,18 38,6"/>
      <polyline points="31,6 38,6 38,13"/>
    </svg>
    <p class="ribbon-label" style="left:160px;width:220px">Know your<br>annual spending</p>
  </div>

  <!-- Step 2 -->
  <div class="ribbon" style="left:372px;top:150px;width:440px;height:110px">
    <svg class="frame" width="440" height="110" viewBox="0 0 440 110" aria-hidden="true">
      <polygon points="40,0 400,0 440,55 400,110 40,110 0,55" fill="var(--navy)"/>
      <polygon points="56,12 384,12 406,55 384,98 56,98 34,55" fill="var(--white)"/>
    </svg>
    <svg class="ribbon-icon" style="left:90px" viewBox="0 0 44 44" aria-hidden="true" fill="none" stroke="var(--icon)" stroke-width="2.2" stroke-linecap="round" stroke-linejoin="round">
      <circle cx="24" cy="15" r="11"/>
      <path d="M27,10.5 h-4.5 a2.2,2.2 0 0 0 0,4.5 h3 a2.2,2.2 0 0 1 0,4.5 H21 M24,8 v14"/>
      <path d="M3,32 h8 l8,4 h10 l10,-6 M11,32 l6,-3 h7"/>
    </svg>
    <p class="ribbon-label" style="left:138px;width:220px">Project<br>special expenses</p>
  </div>

  <!-- Step 3 -->
  <div class="ribbon" style="left:412px;top:281px;width:401px;height:108px">
    <svg class="frame" width="401" height="108" viewBox="0 0 401 108" aria-hidden="true">
      <polygon points="38,0 363,0 401,54 363,108 38,108 0,54" fill="var(--navy)"/>
      <polygon points="54,12 347,12 368,54 347,96 54,96 33,54" fill="var(--white)"/>
    </svg>
    <svg class="ribbon-icon" style="left:68px" viewBox="0 0 44 44" aria-hidden="true" fill="none" stroke="var(--icon)" stroke-width="2" stroke-linecap="round" stroke-linejoin="round">
      <path d="M9,4 h18 l8,8 v28 H9 z"/>
      <path d="M27,4 v8 h8"/>
      <path d="M15,20 h14 M15,25 h14 M15,30 h10"/>
      <path d="M14,12 l2,2 4,-4"/>
    </svg>
    <p class="ribbon-label" style="left:108px;width:220px">Add up your<br>5-year cash needs</p>
  </div>

  <!-- Step 4 -->
  <div class="ribbon" style="left:412px;top:413px;width:401px;height:108px">
    <svg class="frame" width="401" height="108" viewBox="0 0 401 108" aria-hidden="true">
      <polygon points="38,0 363,0 401,54 363,108 38,108 0,54" fill="var(--navy)"/>
      <polygon points="54,12 347,12 368,54 347,96 54,96 33,54" fill="var(--white)"/>
    </svg>
    <svg class="ribbon-icon" style="left:68px" viewBox="0 0 44 44" aria-hidden="true" fill="none" stroke="var(--icon)" stroke-width="2.2" stroke-linecap="round" stroke-linejoin="round">
      <path d="M16,5 h12 l-3,7 h-6 z"/>
      <path d="M19,12 C8,17 5,27 7,34 c1,4 5,6 15,6 s14,-2 15,-6 c2,-7 -1,-17 -12,-22"/>
      <path d="M25,21 h-4.5 a2.2,2.2 0 0 0 0,4.5 h3 a2.2,2.2 0 0 1 0,4.5 H19 M22,18.5 v14"/>
    </svg>
    <p class="ribbon-label" style="left:108px;width:220px">Set them<br>aside in savings</p>
  </div>

  <!-- Step 5 -->
  <div class="ribbon" style="left:375px;top:545px;width:437px;height:108px">
    <svg class="frame" width="437" height="108" viewBox="0 0 437 108" aria-hidden="true">
      <polygon points="38,0 399,0 437,54 399,108 38,108 0,54" fill="var(--navy)"/>
      <polygon points="54,12 383,12 404,54 383,96 54,96 33,54" fill="var(--white)"/>
    </svg>
    <svg class="ribbon-icon" style="left:86px" viewBox="0 0 44 44" aria-hidden="true" fill="none" stroke="var(--icon)" stroke-width="2.2" stroke-linecap="round" stroke-linejoin="round">
      <path d="M22,18 V4 M18,8 l4,-4 4,4"/>
      <path d="M22,18 L9,10 M9,15 V10 h5"/>
      <path d="M22,18 L35,10 M30,10 h5 v5"/>
      <path d="M25,25 h-4.5 a2.2,2.2 0 0 0 0,4.5 h3 a2.2,2.2 0 0 1 0,4.5 H19 M22,22 v18"/>
    </svg>
    <p class="ribbon-label" style="left:128px;width:220px">Invest<br>the rest</p>
  </div>

  <!-- Repeat -->
  <div class="ribbon" style="left:332px;top:676px;width:482px;height:110px">
    <svg class="frame" width="482" height="110" viewBox="0 0 482 110" aria-hidden="true">
      <polygon points="40,0 442,0 482,55 442,110 40,110 0,55" fill="var(--navy)"/>
      <polygon points="56,12 426,12 448,55 426,98 56,98 34,55" fill="var(--white)"/>
    </svg>
    <svg class="ribbon-icon" style="left:108px" viewBox="0 0 44 44" aria-hidden="true" fill="none" stroke="var(--icon)" stroke-width="2.2" stroke-linecap="round" stroke-linejoin="round">
      <circle cx="22" cy="18" r="13"/>
      <circle cx="22" cy="18" r="9.5"/>
      <path d="M25,13.5 h-4.5 a2.2,2.2 0 0 0 0,4.5 h3 a2.2,2.2 0 0 1 0,4.5 H19 M22,11 v14"/>
      <path d="M14,29 l-4,10 5,-2 3,4 3,-9 M30,29 l4,10 -5,-2 -3,4 -3,-9"/>
    </svg>
    <p class="ribbon-label" style="left:160px;width:220px">Recalculate<br>monthly</p>
  </div>

  <section class="result result--navy result--lifestyle">
    <p>Know<br>your lifestyle<br>will be unaffected<br>by the markets for<br>at least 5-years</p>
  </section>
  <section class="result result--slate result--spend">
    <p>Spend<br>intentionally<br>and with Ned</p>
  </section>
  <section class="result result--navy result--base">
    <p>Create a solid<br>base for lifetime<br>cash flow<br>projections</p>
  </section>

</main>
</body>
</html>
```